Design business card for Bright Harbour Coaching!

I am a personal development coach (like a life coach) and corporate trainer and need a professionally designed double sided business card.

It needs to contain the business logo (I'm happy for the designer to choose the layout of the logo as I am still working out the best option myself) and the following information:

Corinne Vashti
Personal Development Coach and Trainer

+61 (0)452 918 637 (written that way)
corinne@bright-harbour.example

www.bright-harbour.example

```html
<!DOCTYPE html>
<html lang="en">
<head>
<meta charset="utf-8">
<title>Bright Harbour Coaching – Business Card</title>
<link rel="stylesheet" href="https://fonts.googleapis.com/css2?family=Cinzel:wght@400;500&family=Questrial&display=swap">
<style>
  :root {
    --teal: #0b6f6b;
    --teal-light: #1a8c88;
    --cream: #eeebe0;
    --grey-stripe: #c9c7bd;
    --ink-light: #f3f1e8;
    --backdrop: #dcdfdf;
  }
  * { margin: 0; padding: 0; box-sizing: border-box; }
  html, body {
    width: 1200px; height: 786px; overflow: hidden;
    background: var(--backdrop);
  }
  .sheet {
    position: relative; width: 1200px; height: 786px;
    display: flex; align-items: center; justify-content: center; gap: 60px;
  }
  .card {
    position: relative; width: 520px; height: 297px;
    border-radius: 16px; overflow: hidden;
    box-shadow: 0 6px 18px rgba(0,0,0,0.18);
  }
  .card-front { background: var(--cream); }
  .card-back { background: var(--teal); }
  .front-waves { position: absolute; inset: 0; width: 100%; height: 100%; }

  .brand {
    position: absolute; display: flex; align-items: center; gap: 12px;
  }
  .brand-dot {
    width: 34px; height: 34px; border-radius: 50%; flex: none;
  }
  .brand-name {
    font-family: "Cinzel", serif; font-weight: 500;
    font-size: 21px; line-height: 1.05; letter-spacing: 0.5px;
    text-transform: uppercase;
  }
  .card-front .brand { left: 200px; top: 34px; }
  .card-front .brand-dot { background: var(--teal); }
  .card-front .brand-name { color: var(--teal); }

  .person {
    position: absolute; left: 30px; top: 174px;
    font-family: "Questrial", sans-serif; color: var(--ink-light);
  }
  .person-name { font-size: 15px; font-weight: 700; letter-spacing: 1px; text-transform: uppercase; margin-bottom: 5px; }
  .person-role { font-size: 12px; line-height: 1.35; }

  .contact {
    position: absolute; left: 196px; top: 190px;
    font-family: "Questrial", sans-serif; color: var(--ink-light);
    font-size: 11.5px; line-height: 1.6;
    white-space: nowrap;
  }
  .contact-label { font-weight: 700; margin-right: 4px; }
  .contact-web { font-weight: 700; }

  .card-back .brand { left: 50%; top: 92px; transform: translateX(-50%); }
  .card-back .brand-dot { background: var(--ink-light); }
  .card-back .brand-name { color: var(--ink-light); font-size: 24px; white-space: nowrap; }
  .back-web {
    position: absolute; left: 0; right: 0; top: 182px; text-align: center;
    font-family: "Questrial", sans-serif; color: var(--ink-light); font-size: 13px; letter-spacing: 0.3px;
  }
</style>
</head>
<body>
<main class="sheet">
  <section class="card card-front">
    <svg class="front-waves" viewBox="0 0 520 297" preserveAspectRatio="none" aria-hidden="true">
      <path fill="var(--grey-stripe)" d="M0,82 C175,92 420,126 520,252 L520,297 L0,297 Z"/>
      <path fill="var(--teal-light)" d="M0,88 C180,98 420,132 520,262 L520,297 L0,297 Z"/>
      <path fill="var(--cream)" d="M0,100 C175,110 408,144 518,297 L0,297 Z"/>
      <path fill="var(--teal)" d="M0,106 C170,116 400,150 506,297 L0,297 Z"/>
    </svg>
    <div class="brand">
      <span class="brand-dot"></span>
      <span class="brand-name">Bright Harbour<br>Coaching</span>
    </div>
    <div class="person">
      <p class="person-name">Corinne Vashti</p>
      <p class="person-role">Personal Development<br>Coach and Trainer</p>
    </div>
    <div class="contact">
      <p><span class="contact-label">T:</span>+61 (0)452 918 637</p>
      <p><span class="contact-label">E:</span>corinne@bright-harbour.example</p>
      <p class="contact-web">www.bright-harbour.example</p>
    </div>
  </section>

  <section class="card card-back">
    <div class="brand">
      <span class="brand-dot"></span>
      <span class="brand-name">Bright Harbour Coaching</span>
    </div>
    <p class="back-web">www.bright-harbour.example</p>
  </section>
</main>
</body>
</html>
```